Glorvanta Letterhead and Template Design

We are looking to freshen up and modernise our business letter heads and cover pages for our documents. Looking at a suit of new designs. I would like a design for:
- Letter Head
- Page 2 follower (for lengthy documents) - fancy
- Page 2 follower (for lengthy documents) - simple version
- Cover Page for reports to sent to client
- Cover Page for internal documents.

Our website is www.glorvanta.com.au.

I have attached a copy of our current brochure for inspiration and our old letter head so you can see what we currently use.

On our Client Cover Page and letter head we would like to include out business awards. Happy for you to change these designs if you have something that would look better. Have also included logos and awards. We won the Meridian Vermin Control Honour in 2022/23 and also in 2019/2020. We were a state finalist in the Quorvel Enterprise Prizes this year logo attached.

We like the emblem to be watermarked into the page in the background.

We want something fresh/clean/modern and classy.

Letter head needs to include our Phone Number: 1300591037
Email: hello@glorvanta.com.au
Text: 0472913508
Website: www.glorvanta.com.au

```html
<!DOCTYPE html>
<html lang="en">
<head>
<meta charset="utf-8">
<title>Glorvanta Stationery Suite</title>
<link rel="stylesheet" href="https://fonts.googleapis.com/css2?family=Source+Sans+3:wght@400;600;700&family=Roboto:wght@400&display=swap">
<style>
  :root {
    --backdrop: #262626;
    --brand-green: #7dc143;
    --brand-green-soft: #8ccb57;
    --paper: #f6f4f4;
    --ink: #3a3a3a;
    --ink-soft: #5a5a5a;
    --watermark-on-paper: #e9eee1;
    --watermark-on-green: rgba(255,255,255,0.14);
    --white: #ffffff;
  }
  * { margin: 0; padding: 0; box-sizing: border-box; }
  html, body { width: 1200px; height: 547px; overflow: hidden; }
  body {
    background: var(--backdrop);
    font-family: "Source Sans 3", Arial, sans-serif;
    position: relative;
  }
  .page {
    position: absolute;
    top: 47px;
    width: 329px;
    height: 464px;
    overflow: hidden;
  }
  .cover { left: 69px; background: var(--brand-green); }
  .letterhead { left: 434px; background: var(--paper); }
  .follower { left: 803px; background: var(--paper); }

  .wordmark {
    position: absolute;
    display: flex;
    align-items: center;
    gap: 5px;
    font-weight: 700;
    letter-spacing: 0.2px;
    line-height: 1;
  }
  .wordmark .mark-dot { border-radius: 50%; flex: none; }
  .cover .wordmark { left: 0; right: 0; justify-content: center; top: 42px; font-size: 27px; color: var(--white); }
  .cover .wordmark .mark-dot { width: 18px; height: 18px; background: var(--white); }
  .letterhead .wordmark { left: 33px; top: 42px; font-size: 15px; color: var(--ink); }
  .letterhead .wordmark .mark-dot { width: 10px; height: 10px; background: var(--brand-green); }
  .follower .wordmark { left: 0; right: 0; justify-content: center; top: 29px; font-size: 15px; color: var(--ink); }
  .follower .wordmark .mark-dot { width: 10px; height: 10px; background: var(--brand-green); }

  .emblem-watermark {
    position: absolute;
    border-radius: 50%;
  }
  .cover .emblem-watermark {
    left: 56px; top: 106px; width: 218px; height: 300px;
    background: radial-gradient(ellipse at center, var(--watermark-on-green) 0%, rgba(255,255,255,0.06) 70%, rgba(255,255,255,0) 100%);
  }
  .letterhead .emblem-watermark {
    left: 112px; top: 118px; width: 210px; height: 308px;
    background: radial-gradient(ellipse at center, var(--watermark-on-paper) 0%, rgba(233,238,225,0.5) 65%, rgba(233,238,225,0) 100%);
  }
  .follower .emblem-watermark {
    left: 56px; top: 115px; width: 218px; height: 305px;
    background: radial-gradient(ellipse at center, var(--watermark-on-paper) 0%, rgba(233,238,225,0.5) 65%, rgba(233,238,225,0) 100%);
  }

  .cover-url {
    position: absolute; left: 0; right: 0; top: 435px;
    text-align: center; color: var(--white);
    font-size: 7px; font-weight: 700; letter-spacing: 0.9px;
  }

  .contact-block {
    position: absolute; left: 223px; top: 27px;
    font-size: 6.3px; line-height: 8.9px; color: var(--ink);
  }
  .contact-block .label { color: var(--brand-green); }

  .salutation {
    position: absolute; left: 33px; top: 112px;
    font-family: "Roboto", Arial, sans-serif;
    font-size: 9.5px; color: var(--ink);
  }
  .letter-body {
    position: absolute; left: 33px; top: 139px; width: 265px;
    font-family: "Roboto", Arial, sans-serif;
    font-size: 5.15px; line-height: 7.9px; color: var(--ink-soft);
    text-align: justify;
  }
  .letter-body p { margin-bottom: 7.9px; }
  .sign-off {
    position: absolute; left: 33px; top: 312px;
    font-family: "Roboto", Arial, sans-serif;
    font-size: 5.4px; color: var(--ink-soft);
  }
  .signature { position: absolute; left: 31px; top: 325px; }
  .signatory {
    position: absolute; left: 35px; top: 350px;
    font-family: "Roboto", Arial, sans-serif; color: var(--ink);
  }
  .signatory .name { font-size: 7.6px; }
  .signatory .role { font-size: 5.8px; margin-top: 2px; color: var(--ink-soft); }

  .award-row { position: absolute; left: 237px; top: 396px; display: flex; gap: 7px; }
  .award { width: 27px; text-align: center; }
  .award .seal {
    width: 24px; height: 24px; margin: 0 auto;
    border-radius: 50%; background: #e2c36a; border: 2px solid #c9a441;
  }
  .award .caption { font-size: 2.6px; line-height: 3px; font-weight: 700; color: var(--ink); margin-top: 2px; }

  .footer-swoosh { position: absolute; left: 0; bottom: 0; width: 329px; height: 50px; }
  .footer-url {
    position: absolute; left: 0; right: 0; top: 452px;
    text-align: center; color: var(--white); font-size: 6.6px;
  }
</style>
</head>
<body>

<section class="page cover">
  <div class="wordmark"><span class="mark-dot"></span>Glorvanta</div>
  <div class="emblem-watermark" role="img" aria-label="Faint company emblem watermark"></div>
  <div class="cover-url">www.glorvanta.com.au</div>
</section>

<section class="page letterhead">
  <div class="emblem-watermark" role="img" aria-label="Faint company emblem watermark"></div>
  <div class="wordmark"><span class="mark-dot"></span>Glorvanta</div>
  <div class="contact-block">
    <div><span class="label">Firm License :</span> 4827</div>
    <div><span class="label">P :</span> 1300591037</div>
    <div><span class="label">T :</span> 0472913508</div>
    <div>hello@glorvanta.com.au</div>
    <div><span class="label">ABN :</span> 51 739 204 168</div>
  </div>

  <div class="salutation">Dear Mr. Harrow,</div>
  <div class="letter-body">
    <p>Lorem ipsum dolor sit amet, consectetur adipiscing elit. Donec orci purus, luctus vitae dignissim eu, iaculis sed purus. Vivamus faucibus, ipsum nec aliquet viverra, leo mauris condimentum ligula, sit amet sagittis enim ligula quis arcu. Nam egestas tortor id nisi porttitor mattis. In tortor ante, ultricies in suscipit a, tempus non massa. Vivamus et auctor mi. Fusce vel massa nulla. Phasellus nec eros mauris, et scelerisque orci.</p>
    <p>Donec malesuada orci vitae nulla accumsan porta a id massa. Quisque accumsan iaculis magna sit amet fringilla. Maecenas consequat, magna eget tincidunt semper, odio nibh rutrum mi, id feugiat ante nisi eu risus. Vestibulum nunc orci, rhoncus a placerat in, ultricies in mi. Cras mattis varius eros, vel fringilla nisi suscipit eget. Quisque scelerisque sagittis nulla at porttitor.</p>
    <p>Sed id augue vitae urna euismod commodo aliquet a quam. Pellentesque arcu velit, cursus et malesuada ut, consequat et diam. Nullam erat sem, rhoncus id ullamcorper vitae, rhoncus et arcu. In ultricies ultricies nulla, ut rutrum nisi iaculis at. Donec eu magna a metus ornare faucibus. Fusce aliquet faucibus ultricies. Morbi semper, est id tincidunt gravida, sem arcu adipiscing lacus, ac bibendum nulla leo eu purus. Quisque nec diam sed risus consectetur a ccumsan quis quis nibh. Vestibulum id purus lorem.</p>
    <p>It is a long established fact that a reader will be distracted by the readable content of a page when looking at its layout. The point of using Lorem Ipsum is that it has a more-or-less normal distribution of letters, as opposed to using 'Content here, content here', making it look like readable English. Many desktop publishing packages</p>
  </div>
  <div class="sign-off">Sincerely,</div>
  <svg class="signature" width="46" height="20" viewBox="0 0 46 20" role="img" aria-label="Signature">
    <path d="M1 9 C10 8 20 7 30 9 C36 10 42 10 45 11 M8 3 C16 2 22 6 20 9 C18 12 28 6 30 11 L31 17" fill="none" stroke="#1d2433" stroke-width="0.9" stroke-linecap="round"/>
  </svg>
  <div class="signatory">
    <div class="name">Ellis Harrow</div>
    <div class="role">CEO/ Founder</div>
  </div>

  <div class="award-row">
    <div class="award"><div class="seal"></div><div class="caption">Meridian Honour 2019/20</div></div>
    <div class="award"><div class="seal"></div><div class="caption">State Honour 2022/23</div></div>
  </div>

  <svg class="footer-swoosh" viewBox="0 0 329 50" preserveAspectRatio="none" aria-hidden="true">
    <path d="M0 0 C80 28 230 30 329 12 L329 50 L0 50 Z" fill="var(--brand-green)"/>
    <path d="M60 24 C150 34 230 30 268 15 C225 34 150 36 60 24 Z" fill="var(--white)"/>
  </svg>
  <div class="footer-url">www.glorvanta.com.au</div>
</section>

<section class="page follower">
  <div class="emblem-watermark" role="img" aria-label="Faint company emblem watermark"></div>
  <div class="wordmark"><span class="mark-dot"></span>Glorvanta</div>
  <svg class="footer-swoosh" viewBox="0 0 329 50" preserveAspectRatio="none" aria-hidden="true">
    <path d="M0 0 C80 28 230 30 329 12 L329 50 L0 50 Z" fill="var(--brand-green)"/>
    <path d="M60 24 C150 34 230 30 268 15 C225 34 150 36 60 24 Z" fill="var(--white)"/>
  </svg>
  <div class="footer-url">www.glorvanta.com.au</div>
</section>

</body>
</html>
```